Korvane Business Cards

We need a business card design. We are a Technology (Audio Visual) design, sales and installation company. Looking for a double sided design, clean

Contact Information for Business Card

Clean, modern look, 2 sided

Font styles to use
Sans Serif

```html
<!DOCTYPE html>
<html lang="en">
<head>
<meta charset="utf-8">
<title>Korvane Business Card</title>
<link rel="stylesheet" href="https://fonts.googleapis.com/css2?family=Oswald:wght@500&family=Source+Sans+3:wght@300;400;600;700&display=swap">
<style>
  :root {
    --page: #e9e6e2;
    --orange: #e8701f;
    --orange-deep: #d95e12;
    --slate: #2c343c;
    --slate-deep: #1c2228;
    --ink: #15191d;
    --white: #ffffff;
    --pale-text: #d9dde0;
    --frost-top: #e4ddd4;
    --frost-bottom: #cfc6bb;
  }
  * { margin: 0; padding: 0; box-sizing: border-box; }
  html, body {
    width: 1200px; height: 969px; overflow: hidden;
    background: var(--page);
    font-family: "Source Sans 3", sans-serif;
  }
  .card {
    position: absolute; left: 141px; top: 222px;
    width: 918px; height: 524px;
    border-radius: 22px; overflow: hidden;
    background: linear-gradient(160deg, var(--frost-top), var(--frost-bottom));
    box-shadow: 0 10px 30px rgba(0,0,0,0.18);
  }
  .identity-panel {
    position: absolute; left: 0; top: 0; width: 439px; height: 261px;
    background: linear-gradient(135deg, var(--orange), var(--orange-deep));
    border-radius: 0 0 12px 0;
  }
  .contact-panel {
    position: absolute; left: 0; top: 268px; width: 439px; height: 256px;
    background: linear-gradient(135deg, var(--slate), var(--slate-deep));
    border-radius: 0 12px 0 0;
  }
  .person-name {
    position: absolute; left: 76px; top: 96px;
    font-family: "Oswald", sans-serif; font-weight: 500;
    font-size: 43px; letter-spacing: 0.5px; line-height: 1;
    color: var(--ink);
  }
  .person-name .surname { color: var(--white); }
  .person-role {
    position: absolute; left: 76px; top: 152px;
    font-size: 20px; font-weight: 600; letter-spacing: 0.5px;
    color: var(--ink);
  }
  .address {
    position: absolute; left: 76px; top: 327px;
    font-size: 20px; font-weight: 300; line-height: 26px; color: var(--pale-text);
  }
  .contact-row {
    position: absolute; left: 76px;
    display: flex; align-items: center; gap: 8px;
    font-size: 20px; font-weight: 300; color: var(--pale-text);
    white-space: nowrap;
  }
  .contact-row svg { width: 16px; height: 16px; fill: var(--orange); flex: none; }
  .row-phone { top: 396px; }
  .row-mobile { top: 422px; }
  .row-web { top: 456px; font-size: 17px; gap: 6px; }
  .row-web svg { width: 14px; height: 14px; }
  .row-web .gap { width: 4px; }
  .brand-name {
    position: absolute; left: 439px; top: 0; width: 479px; height: 524px;
    display: flex; align-items: center; justify-content: center;
    font-weight: 700; font-size: 84px; letter-spacing: -1px;
    color: var(--ink);
  }
</style>
</head>
<body>
  <div class="card">
    <div class="identity-panel"></div>
    <div class="contact-panel"></div>

    <div class="person-name">DANIEL <span class="surname">REYES</span></div>
    <div class="person-role">PRESIDENT</div>

    <div class="address">4120 Alder Court<br>Juneau, Alaska 99801</div>

    <div class="contact-row row-phone">
      <svg viewBox="0 0 16 16" aria-hidden="true"><path d="M3.6 1.2l2.3 2.6-1.3 1.8c.9 2 2.6 3.7 4.6 4.6l1.8-1.3 2.6 2.3-1.2 2.4C7.5 13.4 2.6 8.5 1.2 3.6z"/></svg>
      <span>555-214-7830</span>
    </div>
    <div class="contact-row row-mobile">
      <svg viewBox="0 0 16 16" aria-hidden="true"><path d="M4.5 0h7a1 1 0 0 1 1 1v14a1 1 0 0 1-1 1h-7a1 1 0 0 1-1-1V1a1 1 0 0 1 1-1zm.5 2v10h6V2zm3 11a1 1 0 1 0 0 2 1 1 0 0 0 0-2z"/></svg>
      <span>555-603-1492</span>
    </div>
    <div class="contact-row row-web">
      <svg viewBox="0 0 16 16" aria-hidden="true"><path d="M1 3h14v10H1zm1.5 1.2V12h11V4.2L8 8.6z M2.8 4l5.2 4 5.2-4z"/></svg>
      <span>info@korvane.com</span>
      <span class="gap"></span>
      <svg viewBox="0 0 16 16" aria-hidden="true"><path d="M8 0a8 8 0 1 0 0 16A8 8 0 0 0 8 0zm-1 2.2v2.3H4.2A6 6 0 0 1 7 2.2zm2 0a6 6 0 0 1 2.8 2.3H9zM2.3 6.5H7v3H2.3a6 6 0 0 1 0-3zm6.7 0h4.7a6 6 0 0 1 0 3H9zm-4.8 5H7v2.3a6 6 0 0 1-2.8-2.3zm4.8 0h2.8A6 6 0 0 1 9 13.8z"/></svg>
      <span>www.korvane.com</span>
    </div>

    <div class="brand-name">Korvane</div>
  </div>
</body>
</html>
```